Commercial Solar EPC Contractor Brochure to present to prospective clients

We need a brochure designed for our company to send out to clients. We are a commercial solar epc contractor for ground mount solar, commercial solar rooftop, car ports and also offer operation and maintenance contracts.
We can arrange PPA funding

Please see our website https//: quillmarsh-vantor.test

I would like a modern, crisp brochure showcasing our services

Target Market(s)

Commercial Businesses, Solar PV Market for ground mount and rooftop solar

Industry/Entity Type

Renewable Energy - Solar

Colors
0054AA
0677BA
7BADD7
CADEEF
E8F1F8
00AB8E
00BBA5
67D7C9
C6EFE9
E9F9F6
F0912C
F2A743
F7CA91
FBE8D2
FDF5EE

Requirements
Must have
• Case studies, images, about us section, graphics
Nice to have
• QR code to website,

```html
<!DOCTYPE html>
<html lang="en">
<head>
<meta charset="utf-8">
<title>Quillmarsh Vantor Solar – Brochure</title>
<link href="https://fonts.googleapis.com/css2?family=Montserrat:wght@600;700;800&family=Open+Sans:wght@400;600&display=swap" rel="stylesheet">
<style>
:root{
  --blue-dark:#0054AA;
  --blue:#0677BA;
  --blue-light:#7BADD7;
  --blue-pale:#CADEEF;
  --blue-mist:#E8F1F8;
  --green:#00AB8E;
  --green-mid:#00BBA5;
  --leaf:#6FA33A;
  --orange:#F0912C;
  --orange-mid:#F2A743;
  --orange-pale:#F7CA91;
  --cream:#FDF5EE;
  --ink:#2b3440;
  --paper:#ffffff;
  --bg:#e9ecef;
}
*{box-sizing:border-box;margin:0;padding:0}
html,body{width:1200px;height:3000px;overflow:hidden;background:var(--bg)}
body{font-family:"Open Sans",Arial,sans-serif;color:var(--ink);position:relative}
.spread{position:absolute;left:50px;width:1100px;height:760px;background:var(--paper);box-shadow:0 6px 24px rgba(0,0,0,.18);overflow:hidden}
.spread--cover{top:60px}
.spread--cases{top:1110px}
.spread--process{top:2160px}
.page{position:absolute;top:0;width:550px;height:760px;overflow:hidden}
.page--left{left:0}
.page--right{left:550px}
.fold{position:absolute;left:549px;top:0;width:2px;height:760px;background:rgba(0,0,0,.06);z-index:5}
.photo{position:absolute}
.photo--field{background:linear-gradient(160deg,#8fb86a,#4f7d3c 55%,#2e4f6b)}
.photo--panels{background:linear-gradient(150deg,#bcd8f0,#5d8fc4 40%,#1f4e88)}
.photo--roof{background:linear-gradient(170deg,#a9c7e2,#44617f 60%,#2a3a4d)}
.photo--site{background:linear-gradient(160deg,#c9dcea,#8c9a6c 60%,#5e6d3e)}
.photo--crew{background:linear-gradient(160deg,#dde6ee,#e08a3a 55%,#6b7c48)}
.photo--building{background:linear-gradient(160deg,#e6eef4,#b9c4cc 60%,#7e8b95)}
.footer-band{position:absolute;left:0;bottom:0;width:100%;height:110px}
.brand{position:absolute;display:flex;align-items:center;gap:8px;font-family:"Montserrat",Arial,sans-serif;font-weight:700;color:var(--blue-dark);font-size:15px}
.brand-dot{width:14px;height:14px;border-radius:50%;background:var(--green)}
.contact{position:absolute;font-size:12px;line-height:1.7;color:var(--ink)}
.contact-row{display:flex;align-items:center;gap:8px}
.cover-title{position:absolute;font-family:"Montserrat",Arial,sans-serif;font-weight:800;color:#fff;font-size:30px;line-height:1.15}
.heading{font-family:"Montserrat",Arial,sans-serif;font-weight:700}
.body-text{font-size:11.5px;line-height:1.55}
.green-box{position:absolute;background:var(--leaf);color:#fff;padding:26px 24px}
.green-box h2{font-size:24px;margin-bottom:14px}
.orange-bar{position:absolute;background:var(--orange);color:#fff;padding:12px 20px;font-size:19px}
.blue-panel{position:absolute;background:var(--blue);color:#fff}
.section-label{font-family:"Montserrat",Arial,sans-serif;font-weight:700;color:var(--orange);font-size:13px;margin:10px 0 4px}
.wheel{position:absolute}
.wheel text{font-family:"Montserrat",Arial,sans-serif;font-weight:700}
</style>
</head>
<body>

<!-- Cover spread: back cover + front cover -->
<section class="spread spread--cover">
  <div class="page page--left">
    <div class="photo photo--field" style="left:0;top:0;width:550px;height:330px" role="img" aria-label="Aerial photo of a large ground-mount solar farm among green fields"></div>
    <div class="brand" style="left:40px;top:380px"><span class="brand-dot"></span>Quillmarsh Vantor Solar</div>
    <div class="contact" style="left:40px;top:430px">
      <div class="contact-row">
        <svg width="14" height="14" viewBox="0 0 24 24"><path fill="#0677BA" d="M12 2a7 7 0 0 0-7 7c0 5 7 13 7 13s7-8 7-13a7 7 0 0 0-7-7zm0 9.5A2.5 2.5 0 1 1 12 6.5a2.5 2.5 0 0 1 0 5z"/></svg>
        Unit 4, Marsh Business Park, Harlow Road
      </div>
      <div class="contact-row" style="padding-left:22px">Eastbridge, EB12 4QV</div>
      <div class="contact-row">
        <svg width="14" height="14" viewBox="0 0 24 24"><path fill="#0677BA" d="M6.6 10.8a15 15 0 0 0 6.6 6.6l2.2-2.2c.3-.3.7-.4 1-.2 1.1.4 2.3.6 3.6.6.6 0 1 .4 1 1V20c0 .6-.4 1-1 1A17 17 0 0 1 3 4c0-.6.4-1 1-1h3.5c.6 0 1 .4 1 1 0 1.3.2 2.5.6 3.6.1.3 0 .7-.2 1z"/></svg>
        +00 555 0142 318
      </div>
      <div class="contact-row">
        <svg width="14" height="14" viewBox="0 0 24 24"><path fill="#0677BA" d="M12 2a10 10 0 1 0 0 20 10 10 0 0 0 0-20zm6.9 6h-3a15 15 0 0 0-1.3-3.9A8 8 0 0 1 18.9 8zM12 4c.8 1.2 1.5 2.5 1.9 4h-3.8c.4-1.5 1.1-2.8 1.9-4zM4.3 14a8 8 0 0 1 0-4h3.4a16 16 0 0 0 0 4zm.8 2h3a15 15 0 0 0 1.3 3.9A8 8 0 0 1 5.1 16zm3-8h-3a8 8 0 0 1 4.3-3.9A15 15 0 0 0 8.1 8zM12 20c-.8-1.2-1.5-2.5-1.9-4h3.8c-.4 1.5-1.1 2.8-1.9 4zm2.3-6H9.7a14 14 0 0 1 0-4h4.6a14 14 0 0 1 0 4zm.3 5.9a15 15 0 0 0 1.3-3.9h3a8 8 0 0 1-4.3 3.9zm1.7-5.9a16 16 0 0 0 0-4h3.4a8 8 0 0 1 0 4z"/></svg>
        quillmarsh-vantor.test
      </div>
    </div>
    <svg class="footer-band" viewBox="0 0 550 110" preserveAspectRatio="none">
      <path d="M0 40 Q275 0 550 30 L550 110 L0 110Z" fill="var(--blue-pale)"/>
      <path d="M0 58 Q275 22 550 50 L550 110 L0 110Z" fill="var(--blue)"/>
    </svg>
  </div>

  <div class="page page--right">
    <div class="photo photo--panels" style="left:0;top:0;width:550px;height:470px" role="img" aria-label="Close view of solar panel rows under a blue sky"></div>
    <svg style="position:absolute;left:0;top:300px" width="550" height="250" viewBox="0 0 550 250">
      <path d="M140 40 L550 0 L550 190 L110 230Z" fill="var(--leaf)"/>
      <path d="M110 230 L550 190 L550 200 L110 240Z" fill="var(--blue-pale)"/>
    </svg>
    <div class="cover-title" style="left:175px;top:360px;width:350px">Solar Contracting &amp;<br>Development<br>Engineering</div>
    <div class="brand" style="left:300px;top:600px"><span class="brand-dot"></span>Quillmarsh Vantor Solar</div>
    <svg class="footer-band" viewBox="0 0 550 110" preserveAspectRatio="none">
      <path d="M0 30 Q275 0 550 40 L550 110 L0 110Z" fill="var(--blue-pale)"/>
      <path d="M0 50 Q275 22 550 58 L550 110 L0 110Z" fill="var(--blue)"/>
    </svg>
  </div>
  <div class="fold"></div>
</section>

<!-- Inside spread: case studies -->
<section class="spread spread--cases">
  <div class="page page--left">
    <div class="photo photo--roof" style="left:0;top:60px;width:550px;height:280px" role="img" aria-label="Rooftop solar installation on an estate building"></div>
    <div class="green-box" style="left:0;top:0;width:250px;height:480px">
      <h2 class="heading">Harrowfield Estate</h2>
      <p class="body-text">A 250 kWp rooftop array designed, supplied and installed on the estate's farm buildings, cutting grid demand by almost half across the year.</p>
      <p class="body-text" style="margin-top:12px">Delivered on a PPA model with no upfront cost to the client and a full operation and maintenance contract.</p>
      <p class="body-text" style="margin-top:12px;font-weight:600">Completed in eight weeks, fully commissioned.</p>
    </div>
    <div class="photo photo--building" style="left:270px;top:360px;width:130px;height:110px" role="img" aria-label="Estate building with panels on roof"></div>
    <div class="photo photo--site" style="left:410px;top:360px;width:120px;height:110px" role="img" aria-label="Inverter room on site"></div>
    <div class="blue-panel" style="left:0;top:500px;width:550px;height:260px;padding:30px 40px">
      <p class="body-text">Every project follows our turnkey process, from site survey and grid application to installation, commissioning and long-term monitoring.</p>
    </div>
  </div>

  <div class="page page--right">
    <div class="orange-bar heading" style="left:50px;top:30px;width:470px">Brennock Resource Centre</div>
    <div class="photo photo--roof" style="left:30px;top:90px;width:300px;height:170px" role="img" aria-label="Solar panels on the resource centre roof"></div>
    <div class="photo photo--crew" style="left:345px;top:90px;width:175px;height:170px" role="img" aria-label="Installation crew working on site"></div>
    <div style="position:absolute;left:30px;top:275px;width:490px">
      <p class="body-text">A 150 kWp rooftop system supplying the centre's daytime load, with a battery store and live monitoring dashboard for facility staff.</p>
    </div>
    <div class="photo photo--site" style="left:30px;top:345px;width:230px;height:130px" role="img" aria-label="Ground works for solar farm"></div>
    <div class="photo photo--field" style="left:275px;top:345px;width:245px;height:130px" role="img" aria-label="Completed solar farm rows"></div>
    <div class="blue-panel" style="left:0;top:500px;width:550px;height:260px;padding:30px 40px">
      <h3 class="heading" style="font-size:22px;margin-bottom:12px">30 MW Solar Farm</h3>
      <p class="body-text">Full EPC delivery of a ground-mount solar farm, including civil works, substation connection and a ten-year operation and maintenance agreement.</p>
    </div>
  </div>
  <div class="fold"></div>
</section>

<!-- Inside spread: process -->
<section class="spread spread--process">
  <div class="page page--left">
    <div class="blue-panel heading" style="left:40px;top:40px;width:470px;height:44px;padding:11px 20px;font-size:18px">The EPC Turnkey Model</div>
    <svg class="wheel" style="left:55px;top:110px" width="440" height="440" viewBox="0 0 440 440">
      <rect x="0" y="0" width="215" height="215" rx="24" fill="var(--leaf)"/>
      <rect x="225" y="0" width="215" height="215" rx="24" fill="var(--orange-mid)"/>
      <rect x="0" y="225" width="215" height="215" rx="24" fill="var(--blue)"/>
      <rect x="225" y="225" width="215" height="215" rx="24" fill="var(--orange)"/>
      <circle cx="220" cy="220" r="150" fill="var(--cream)"/>
      <circle cx="220" cy="220" r="150" fill="none" stroke="var(--orange-pale)" stroke-width="28"/>
      <circle cx="220" cy="220" r="62" fill="#fff" stroke="var(--blue-pale)" stroke-width="4"/>
      <text x="220" y="224" text-anchor="middle" font-size="14" fill="var(--blue-dark)">EPC</text>
      <text x="40" y="50" font-size="13" fill="#fff">Design</text>
      <text x="330" y="50" font-size="13" fill="#fff">Procure</text>
      <text x="40" y="405" font-size="13" fill="#fff">Maintain</text>
      <text x="340" y="405" font-size="13" fill="#fff">Build</text>
      <text x="220" y="130" text-anchor="middle" font-size="11" fill="var(--ink)">Feasibility</text>
      <text x="300" y="224" text-anchor="middle" font-size="11" fill="var(--ink)">Funding</text>
      <text x="220" y="320" text-anchor="middle" font-size="11" fill="var(--ink)">Commission</text>
      <text x="140" y="224" text-anchor="middle" font-size="11" fill="var(--ink)">Monitor</text>
    </svg>
    <div class="blue-panel" style="left:0;top:580px;width:550px;height:180px;padding:26px 40px">
      <p class="body-text">One contract, one point of contact: we handle design, procurement, construction and aftercare so your project runs to time and budget.</p>
    </div>
  </div>

  <div class="page page--right">
    <h2 class="heading" style="position:absolute;left:40px;top:40px;font-size:26px;color:var(--blue-dark)">Project Management</h2>
    <div style="position:absolute;left:40px;top:90px;width:470px">
      <p class="section-label">Planning &amp; Design</p>
      <p class="body-text">Our engineers survey each site and model yield to size the system for your load profile and roof or land area.</p>
      <p class="section-label">Funding &amp; PPA</p>
      <p class="body-text">We arrange power purchase agreements so clients can go solar with no capital outlay.</p>
      <p class="section-label">Operation &amp; Maintenance</p>
      <p class="body-text">Scheduled servicing, cleaning and remote monitoring keep output high for the life of the plant.</p>
    </div>
    <div class="photo photo--panels" style="left:40px;top:380px;width:470px;height:190px" role="img" aria-label="Rows of ground-mounted solar panels beside trees"></div>
    <div class="blue-panel" style="left:0;top:580px;width:550px;height:180px;padding:26px 40px">
      <p class="body-text">Talk to our team about ground mount, rooftop and carport solar for your business.</p>
    </div>
  </div>
  <div class="fold"></div>
</section>

</body>
</html>
```